Cedar Hollow responsive web design

We need a responsive, bootstrap compatible (but design only - PSD files) website design for a fly fishing shop and guide service.

Design should be very clean. Home Page design + interior page design please.

Possible Home Page Content:
Slide Show
Highlight Three Features: Guided Trips, Fly Shop, Missouri River
About

Thank you and good luck!

Shop

• This will be used on Bootstrap CMS so needs 12 column bootstrap measurements.

DESIGN ONLY NEEDED (clean PSD files), no programming required.
Need a Home Page layout and secondary page layout

Must show use of the following:
H1 - H5 font uses
link color
Dropdown for navigation bar
Button example
• No cutout images, this will be part of CMS and client needs to be able to update most content without knowing photoshop.

```html
<!DOCTYPE html>
<html lang="en">
<head>
<meta charset="utf-8">
<title>Cedar Hollow — Fly Shop &amp; Guide Service</title>
<link rel="stylesheet" href="https://fonts.googleapis.com/css2?family=Open+Sans:wght@400;600;700&display=swap">
<style>
:root{
  --sky:#7dd0f0;
  --sky-deep:#4aaed8;
  --sky-pale:#c3ebf9;
  --sand:#ebe1be;
  --sand-frame:#d5c8a0;
  --call-bg:#ede0bd;
  --plum:#2b1a22;
  --ink:#222;
  --text:#3a3a3a;
  --muted:#666;
  --footer:#2b2b2b;
  --footer-link:#e6dab6;
  --white:#fff;
}
*{box-sizing:border-box;margin:0;padding:0}
html,body{width:1010px;height:1200px;overflow:hidden}
body{font-family:"Open Sans",Arial,sans-serif;background:var(--white);position:relative;color:var(--text)}
h1,h2,h3{font-weight:400}
.top-wash{position:absolute;left:0;top:0;width:1010px;height:470px;background:linear-gradient(var(--sky-pale),#e6f6fc 55%,var(--white))}
.brand{position:absolute;left:62px;top:34px;display:flex;align-items:center;gap:8px;font-size:22px;font-weight:700;color:var(--ink)}
.brand-mark{width:14px;height:14px;background:var(--sky)}
.call-box{position:absolute;left:779px;top:3px;width:168px;height:34px;background:var(--call-bg);display:flex;align-items:center;gap:8px;padding-left:9px;font-size:12px;color:#666;white-space:nowrap}
.call-box strong{color:var(--ink);font-weight:600}
.main-nav{position:absolute;top:64px;right:51px;display:flex;font-size:11px;text-transform:uppercase;white-space:nowrap}
.main-nav a{display:block;padding:0 11px;line-height:31px;color:var(--ink);text-decoration:none}
.main-nav .active{background:var(--plum);color:var(--white);font-weight:600;border-radius:2px}
.dropdown{position:absolute;left:660px;top:106px;width:151px;height:98px;background:var(--plum);z-index:5;padding:9px 0 0 30px;list-style:none;border-radius:2px}
.dropdown::before{content:"";position:absolute;left:68px;top:-7px;border:7px solid transparent;border-top:0;border-bottom-color:var(--plum)}
.dropdown li{font-size:11px;color:var(--white);line-height:20.3px;white-space:nowrap}
.slider{position:absolute;left:61px;top:105px;width:888px;height:351px;background:var(--white);border:1px solid #dfe7ea;padding:4px}
.slide-photo{width:100%;height:100%;background:linear-gradient(120deg,#8a6a3c,#b98e4e 45%,#6d6a5c 70%,#c2a067)}
.slide-caption{position:absolute;left:5px;top:194px;width:443px;height:52px;background:var(--sky);font-size:26px;font-weight:400;color:var(--ink);padding-left:19px;line-height:50px;white-space:nowrap;overflow:hidden}
.slide-dots{position:absolute;left:416px;top:318px;display:flex;gap:5px}
.slide-dots span{width:10px;height:10px;border-radius:50%;background:var(--white)}
.slide-dots .on{background:#f0d9a0}
.about{position:absolute;left:62px;top:484px;width:886px;text-align:center}
.section-title{font-size:20px;font-weight:400;color:#444;text-transform:uppercase}
.about p{margin-top:11px;font-size:11px;line-height:18px;color:var(--muted)}
.features{position:absolute;left:0;top:607px;width:1010px;height:357px;background:var(--sand)}
.features .section-title{position:absolute;top:23px;width:100%;text-align:center}
.feature{position:absolute;top:72px;width:262px}
.feature-photo{position:relative;height:149px;border:4px solid var(--sand-frame)}
.feature-photo .fill{width:100%;height:100%}
.feature-label{position:absolute;left:0;bottom:0;width:100%;height:34px;background:rgba(0,0,0,.72);color:var(--white);font-size:16px;font-weight:600;padding-left:11px;line-height:34px}
.feature p{margin-top:11px;font-size:11.5px;line-height:18px;color:var(--text);letter-spacing:-.1px}
.btn{display:inline-block;margin-top:17px;width:98px;height:28px;background:var(--sky);border:1px solid var(--sky-deep);font-size:12px;color:var(--ink);text-align:center;line-height:26px}
.newsletter{position:absolute;left:0;top:964px;width:1010px;height:81px;background:#80d3f2;border-top:2px solid #5fbde4}
.newsletter h3{position:absolute;left:62px;top:28px;font-size:20px;font-weight:400;color:var(--ink)}
.email-field{position:absolute;left:285px;top:19px;width:662px;height:42px;background:linear-gradient(#f4f4f4,var(--white));border:1px solid #b8dfee;font-size:13px;color:#888;padding-left:13px;line-height:40px}
.subscribe{position:absolute;right:6px;top:6px;width:125px;height:30px;background:#2a2a2a;color:var(--white);font-size:12px;font-weight:600;text-align:center;line-height:30px}
.site-footer{position:absolute;left:0;top:1045px;width:1010px;height:155px;background:var(--footer)}
.footer-nav{position:absolute;left:62px;top:29px;display:flex;gap:23px;font-size:11px;color:var(--footer-link)}
.connect{position:absolute;left:829px;top:26px;font-size:13px;color:var(--footer-link)}
.social{position:absolute;left:830px;top:52px;display:flex;gap:7px}
.social span{width:24px;height:24px;border-radius:50%;background:#555}
.footer-brand{position:absolute;left:62px;top:99px;display:flex;align-items:center;gap:6px;font-size:12px;font-weight:700;color:var(--sky);white-space:nowrap}
.footer-brand .brand-mark{width:10px;height:10px}
.copyright{position:absolute;left:171px;top:100px;font-size:9px;line-height:15px;color:#888}
.copyright a{color:var(--sky);text-decoration:none}
</style>
</head>
<body>
<div class="top-wash"></div>

<header>
  <div class="brand"><span class="brand-mark"></span>Cedar Hollow</div>
  <div class="call-box">
    <svg width="14" height="14" viewBox="0 0 14 14"><rect width="14" height="14" rx="2" fill="#555"/><path d="M4 3.5c1 0 1.4 1.8 1 2.3-.3.4-.6.5-.3 1.2.4.8 1 1.4 1.8 1.8.6.3.9 0 1.2-.3.5-.4 2.3 0 2.3 1 0 .8-.9 1.5-1.8 1.5C5.6 11 3 8.4 3 5.3c0-.9.3-1.8 1-1.8z" fill="#ede0bd"/></svg>
    <span>CALL US: <strong>555 014 2200</strong></span>
  </div>
  <nav class="main-nav">
    <a>Home</a><a>Fly Shop</a><a class="active">Guide Service</a><a>Missouri River</a><a>Contact</a>
  </nav>
  <ul class="dropdown">
    <li>Dropdown menu 1</li><li>Dropdown menu 2</li><li>Dropdown menu 3</li><li>Dropdown menu 4</li>
  </ul>
</header>

<section class="slider">
  <div class="slide-photo" role="img" aria-label="Interior of the fly fishing shop with wooden display tables and tackle racks"></div>
  <h1 class="slide-caption">Welcome to Our Fly Fishing Shop</h1>
  <div class="slide-dots"><span class="on"></span><span></span><span></span><span></span></div>
</section>

<section class="about">
  <h2 class="section-title">Welcome to Cedar Hollow</h2>
  <p>Aliquam molestie, mi et imperdiet euismod, dui purus auctor tellus, et interdum lacus lectus et ante. Sed accumsan sollicitudin sapien, sit amet adipiscing turpis gravida ac. In congue, neque ac lobortis volutpat, libero mauris varius mi, vitae suscipit ipsum ligula vitae risus. Duis aliquam nibh a dui iaculis viverra id a velit. Vivamus egestas risus in magna varius commodo. Sed semper viverra egestas. Etiam pretium porttitor lectus, vel ornare neque porta volutpat.</p>
</section>

<section class="features">
  <h2 class="section-title">Our Main Features</h2>
  <article class="feature" style="left:62px">
    <div class="feature-photo"><div class="fill" role="img" aria-label="Two anglers in a boat on a river beneath rocky hills" style="background:linear-gradient(#a8b8c4,#8f7f62 45%,#4a5560)"></div><h3 class="feature-label">Guided Trips</h3></div>
    <p>Aliquam molestie, mi et imperdiet euismod, dui purus auctor tellus, et interdum lacus lectus et ante. Sed accumsan sollicitudin sapien...</p>
    <a class="btn">Learn More</a>
  </article>
  <article class="feature" style="left:373px">
    <div class="feature-photo"><div class="fill" role="img" aria-label="Fly shop sales floor with wooden fixtures" style="background:linear-gradient(120deg,#8a6a3c,#c09a5c 50%,#6e7470)"></div><h3 class="feature-label">Fly Shop</h3></div>
    <p>Aliquam molestie, mi et imperdiet euismod, dui purus auctor tellus, et interdum lacus lectus et ante. Sed accumsan sollicitudin sapien...</p>
    <a class="btn">Learn More</a>
  </article>
  <article class="feature" style="left:686px">
    <div class="feature-photo"><div class="fill" role="img" aria-label="Missouri River with a forested rocky bluff" style="background:linear-gradient(#aec6dc,#7c8560 40%,#a07a52 60%,#4d5a5e)"></div><h3 class="feature-label">Missouri River</h3></div>
    <p>Aliquam molestie, mi et imperdiet euismod, dui purus auctor tellus, et interdum lacus lectus et ante. Sed accumsan sollicitudin sapien...</p>
    <a class="btn">Learn More</a>
  </article>
</section>

<section class="newsletter">
  <h3>NEWSLETTER SIGNUP</h3>
  <div class="email-field">Enter Email Address<span class="subscribe">SUBSCRIBE</span></div>
</section>

<footer class="site-footer">
  <nav class="footer-nav"><span>Home</span><span>Fly shop</span><span>Guide service</span><span>Missouri river</span><span>Contact</span></nav>
  <div class="connect">Connect Us</div>
  <div class="social" aria-label="Social links"><span></span><span></span><span></span><span></span></div>
  <div class="footer-brand"><span class="brand-mark"></span>Cedar Hollow</div>
  <div class="copyright">Copyright © 2014. <a>Cedar Hollow</a><br>All Right Reserved</div>
</footer>
</body>
</html>
```